Valquor.com Personal Trainer/Fitness Website

I want a website to market my personal training/Outdoor Bootcamp Class services, as well as to ditribute nutrabel. I need a logo as well I included an address for the Bramford Gales 1975 logo. I'd like Valquor in place of Bramford Gales, and in Black and white, just different enough so I can't get sued by the PBL.
https://www.lookfindr-example.net/imgview?src=http%3A%2F%2Fwww.dorian-phelkamp-example.com%2Fmedia%2Fuploads%2F2014%2F01%2Fgales_logo4.jpg&ref=http%3A%2F%2Fwww.dorian-phelkamp-example.com%2Fpbl-logo-redesigns-harbor-storm%2F&id=_kqvxx8PLRbWmNc&tb=z3wqT7KbRsJpYL%3A&w=600&h=450&client=mobile-android&bih=512&biw=360&ved=0bXYfQrTpLmVnWsKdQzHyUeRtAbCdEfGhIjKlMn&iact=mrc&uact=8.
It should be about 5 pages 1. home 2. about 3. Services 4. Blog/Videos and programs 5. Contact.
http://www.brenvoltraining.co.uk/ is a website I like the style of.

Target Market(s)

Seattle area

Industry/Entity Type

Fitness

Coding

Number of Pages Required

Font styles to use
Serif
Sans Serif

Requirements
Must have
• A minimal look
Nice to have
• A logo similar to the 1975 Bramford Galeforce Logo, with a Small Rowan Pell ripping his shirt open(with a picture of the logo on his shirt, picture within picture) to turn into Ironwing in the center. Skyline is black, Background and small figure white(with black logo on shirt)

```html
<!DOCTYPE html>
<html lang="en">
<head>
<meta charset="utf-8">
<title>Valquor – Personal Training &amp; Outdoor Bootcamp</title>
<link href="https://fonts.googleapis.com/css2?family=Open+Sans:ital,wght@0,400;0,600;1,400&family=Roboto:wght@400;500;700&display=swap" rel="stylesheet">
<style>
:root{
  --white:#ffffff;
  --ink:#1d1d1d;
  --grey-text:#666666;
  --muted:#8a8a8a;
  --line:#d9d9d9;
  --soft-bg:#eeeeee;
  --footer-bg:#222222;
  --footer-base:#151515;
  --footer-text:#aaaaaa;
  --accent-yellow:#e6b400;
}
*{margin:0;padding:0;box-sizing:border-box}
html,body{width:1200px;height:2381px;overflow:hidden}
body{position:relative;background:var(--white);font-family:'Open Sans',Arial,sans-serif;color:var(--ink)}
h1,h2,h3,h4{font-weight:400}
.abs{position:absolute}
.heading{font-family:'Roboto',Arial,sans-serif}

/* hero */
.hero{position:absolute;left:0;top:0;width:1200px;height:597px;overflow:hidden}
.hero-photo{position:absolute;inset:0;background:
  radial-gradient(ellipse at 60% 55%,#6b6b6b 0%,transparent 55%),
  linear-gradient(100deg,#2a2a2a 0%,#555 40%,#3a3a3a 70%,#1e1e1e 100%)}
.nav-rule{position:absolute;height:1px;background:rgba(255,255,255,.55)}
.nav-link{position:absolute;top:76px;font-family:'Roboto',Arial,sans-serif;font-weight:500;font-size:14px;color:var(--white);letter-spacing:.3px}
.brand-mark{position:absolute;left:560px;top:18px;width:80px;height:80px;border-radius:50%;background:var(--white)}
.brand-name{position:absolute;left:0;width:1200px;top:102px;text-align:center;font-family:'Roboto',Arial,sans-serif;font-weight:700;font-size:36px;color:var(--white);letter-spacing:1px}
.hero-title{position:absolute;left:0;width:1200px;text-align:center;color:var(--white);font-family:'Roboto',Arial,sans-serif}
.hero-title.line1{top:262px;font-size:48px;font-weight:700;letter-spacing:1px}
.hero-title.line2{top:324px;font-size:31px;font-weight:500}
.btn-outline{position:absolute;display:flex;align-items:center;justify-content:center;font-family:'Roboto',Arial,sans-serif;font-size:13px;text-transform:uppercase}
.btn-hero{left:533px;top:381px;width:134px;height:36px;border:2px solid var(--white);color:var(--white);font-size:14px}
.dots{position:absolute;display:flex;gap:4px}
.dot{width:15px;height:15px;border-radius:50%;background:var(--white)}
.dot.hollow{background:transparent;border:2px solid var(--white)}

/* welcome */
.welcome-photo{left:181px;top:670px;width:262px;height:247px;background:linear-gradient(160deg,#5a5a5a,#2a2a2a 60%,#777)}
.welcome-title{left:481px;top:668px;font-size:30px;color:#6a6a6a}
.welcome-title strong{color:var(--ink);font-weight:500}
.welcome-lead{left:484px;top:722px;width:520px;font-size:13px;line-height:21px;color:#555}
.welcome-copy{left:484px;top:776px;width:520px;font-size:12px;line-height:19.5px;color:var(--grey-text)}
.btn-dark{border:2px solid #333;color:var(--ink)}

/* services */
.services{position:absolute;left:0;top:1002px;width:1200px;height:404px;overflow:hidden}
.services-photo{position:absolute;inset:0;background:
  radial-gradient(ellipse at 50% 45%,#5e4a40 0%,transparent 45%),
  linear-gradient(90deg,#1e1e22,#34333a 40%,#2b2a30 70%,#1a1a1e)}
.section-title{position:absolute;left:0;width:1200px;text-align:center;font-family:'Roboto',Arial,sans-serif}
.service-icon{position:absolute;width:94px;height:94px;border-radius:50%;background:radial-gradient(circle at 40% 35%,#ffffff,#d5d5d5);display:flex;align-items:center;justify-content:center}
.service-name{position:absolute;width:280px;text-align:center;font-family:'Roboto',Arial,sans-serif;font-size:20px;color:var(--white)}
.service-copy{position:absolute;width:240px;text-align:center;font-size:12.5px;line-height:21px;color:#b5b5b5}
.btn-light{border:2px solid var(--white);color:var(--white);width:108px;height:31px}

/* blogs */
.blog-photo{position:absolute;width:199px;height:185px}
.blog-title{position:absolute;width:200px;font-size:15px;line-height:21px;color:var(--ink)}
.blog-copy{position:absolute;width:180px;font-size:12px;line-height:20px;color:#999}
.blog-more{position:absolute;font-family:'Roboto',Arial,sans-serif;font-size:12px;color:#555;font-weight:500}

/* testimonials */
.testimonials{position:absolute;left:0;top:1773px;width:1200px;height:325px;background:var(--soft-bg)}
.quote-mark{position:absolute;font-family:Georgia,serif;font-size:54px;color:#999;line-height:1}
.quote-text{position:absolute;left:250px;top:110px;width:700px;text-align:center;font-style:italic;font-size:13px;line-height:25px;color:#8a8a8a}
.avatar{position:absolute;left:527px;top:200px;width:44px;height:44px;border-radius:50%;background:linear-gradient(#c9b7a8,#8f7b6c);border:2px solid var(--white)}
.author{position:absolute;left:581px;top:201px;font-size:14px;color:var(--ink)}
.author small{display:block;font-size:12px;color:#555;margin-top:4px}
.t-dots{left:572px;top:262px;gap:3px}
.t-dots .dot{width:11px;height:11px;background:transparent;border:1px solid #aaa}
.t-dots .dot.on{border:2px solid #557799}

/* footer */
.footer{position:absolute;left:0;top:2098px;width:1200px;height:227px;background:var(--footer-bg)}
.footer-head{position:absolute;top:44px;font-family:'Roboto',Arial,sans-serif;font-size:15px;color:var(--white);text-transform:uppercase}
.footer-list{position:absolute;top:74px;list-style:none;font-size:11.5px;line-height:21.5px;color:var(--footer-text)}
.footer-divider{position:absolute;top:44px;width:1px;height:140px;background:#333}
.tweet{position:absolute;width:180px;font-size:10px;line-height:20px;color:var(--footer-text);padding-left:28px;white-space:nowrap}
.tweet-handle{color:var(--accent-yellow)}
.tweet-icon{position:absolute;left:0;top:3px;width:14px;height:14px;border-radius:2px;background:#ddd}
.contact-line{position:absolute;font-size:11.5px;line-height:21px;color:var(--footer-text)}
.social{position:absolute;left:905px;top:76px;display:flex;gap:4px}
.social span{width:24px;height:24px;border-radius:50%;border:1.5px solid #ddd}
.footer-base{position:absolute;left:0;top:2325px;width:1200px;height:56px;background:var(--footer-base)}
.copyright{position:absolute;left:203px;top:14px;font-size:11px;color:#bbb}
</style>
</head>
<body>

<header class="hero">
  <div class="hero-photo" role="img" aria-label="Trainer spotting a woman lifting dumbbells on a bench in a gym"></div>
  <div class="nav-rule" style="left:179px;top:60px;width:292px"></div>
  <div class="nav-rule" style="left:179px;top:108px;width:292px"></div>
  <div class="nav-rule" style="left:717px;top:60px;width:299px"></div>
  <div class="nav-rule" style="left:717px;top:108px;width:299px"></div>
  <nav>
    <span class="nav-link" style="left:202px">HOME</span>
    <span class="nav-link" style="left:283px">ABOUT US</span>
    <span class="nav-link" style="left:392px">SERVICES</span>
    <span class="nav-link" style="left:725px">BLOG</span>
    <span class="nav-link" style="left:801px">VIDEOS</span>
    <span class="nav-link" style="left:892px">CONTACT</span>
  </nav>
  <div class="brand-mark"></div>
  <div class="brand-name">VALQUOR</div>
  <h1 class="hero-title line1">PERSONAL TRAINING &amp;</h1>
  <h2 class="hero-title line2">OUTDOOR BOOTCAMP CLASS</h2>
  <a class="btn-outline btn-hero">Learn More</a>
  <div class="dots" style="left:563px;top:570px">
    <span class="dot hollow"></span><span class="dot"></span><span class="dot"></span><span class="dot"></span>
  </div>
</header>

<section class="welcome">
  <div class="abs welcome-photo" role="img" aria-label="Man training on a cable machine in a gym"></div>
  <h2 class="abs heading welcome-title">WELCOME TO <strong>VALQUOR</strong></h2>
  <p class="abs welcome-lead">At justo id velit placerat molestie Donec dictum lectus non odio Cras a ante vitae enim iaculis aliquam Mauris nunc quam venenatis nec euismod</p>
  <p class="abs welcome-copy">egestas placerat est Pellentesque habitant morbi tristique senectus et netus et malesuada fames ac turpis egestas Cras id elit Integer quis urna Ut ante enim dapibus malesuada fringilla eu condimentum quis tellus Aenean porttitor eros vel dolor Donec convallis pede venenatis nibh Duis quam Nam eget lacus Aliquam erat volutpat Quisque dignissim</p>
  <a class="btn-outline btn-dark" style="left:482px;top:879px;width:121px;height:37px">Read More</a>
</section>

<section class="services">
  <div class="services-photo" role="img" aria-label="Muscular athlete lifting a barbell, dark gym background"></div>
  <h2 class="section-title" style="top:36px;font-size:25px;color:var(--white)">OUR SERVICES</h2>

  <div class="service-icon" style="left:282px;top:105px">
    <svg width="48" height="30" viewBox="0 0 48 30"><g fill="none" stroke="#222" stroke-width="2.5"><rect x="4" y="5" width="6" height="20" rx="1"/><rect x="38" y="5" width="6" height="20" rx="1"/><line x1="10" y1="15" x2="38" y2="15"/><line x1="0" y1="15" x2="4" y2="15"/><line x1="44" y1="15" x2="48" y2="15"/></g></svg>
  </div>
  <div class="service-icon" style="left:547px;top:105px">
    <svg width="46" height="38" viewBox="0 0 46 38"><g fill="none" stroke="#222" stroke-width="2.5" stroke-linejoin="round"><path d="M3 35 L23 3 L43 35 Z"/><path d="M23 3 L23 35"/><path d="M17 35 L23 22 L29 35"/></g></svg>
  </div>
  <div class="service-icon" style="left:829px;top:105px">
    <svg width="40" height="40" viewBox="0 0 40 40"><rect x="14" y="16" width="24" height="22" fill="#222"/><path d="M4 30 L12 20 L20 26 L34 6" fill="none" stroke="#222" stroke-width="3"/></svg>
  </div>

  <h3 class="service-name" style="left:189px;top:215px">Personal Training</h3>
  <h3 class="service-name" style="left:454px;top:215px">Outdoor Bootcamp</h3>
  <h3 class="service-name" style="left:736px;top:215px">Fitness Coaching</h3>
  <p class="service-copy" style="left:209px;top:245px">Duis quam Nam eget lacus Aliquam erat volutpat Quisque dignissim</p>
  <p class="service-copy" style="left:474px;top:245px">Duis quam Nam eget lacus Aliquam erat volutpat Quisque dignissim</p>
  <p class="service-copy" style="left:756px;top:245px">Duis quam Nam eget lacus Aliquam erat volutpat Quisque dignissim</p>
  <a class="btn-outline btn-light" style="left:270px;top:303px">Read More</a>
  <a class="btn-outline btn-light" style="left:547px;top:303px">Read More</a>
  <a class="btn-outline btn-light" style="left:827px;top:303px">Read More</a>

  <svg class="abs" style="left:0;top:340px" width="1200" height="64" viewBox="0 0 1200 64" aria-hidden="true"><path d="M0 10 L600 64 L1200 10 L1200 64 L0 64 Z" fill="#fff"/></svg>
</section>

<section class="blogs">
  <h2 class="section-title" style="top:1452px;font-size:25px;color:var(--ink)">LATEST BLOGS</h2>

  <div class="blog-photo" style="left:179px;top:1521px;background:linear-gradient(135deg,#4a3a30,#8a7a6c 50%,#2e2a28)" role="img" aria-label="Trainer writing on a clipboard with a client in a gym"></div>
  <h3 class="blog-title" style="left:397px;top:1522px">Eger quis urna Ut ante enim dapibus</h3>
  <p class="blog-copy" style="left:397px;top:1572px">fringilla eu condimentum quis tellus Aenean porttitor eros vel dolor Donec convallis pede venenatis nibh Duis quam Nam eget lacus Aliquam erat</p>
  <span class="blog-more" style="left:397px;top:1688px">READ MORE</span>

  <div class="blog-photo" style="left:616px;top:1521px;background:linear-gradient(135deg,#d9d2c6,#a59c90 50%,#4a4a5a)" role="img" aria-label="Woman doing sit-ups on a mat with a trainer"></div>
  <h3 class="blog-title" style="left:833px;top:1522px">Cum sociis natoque penatibus magnis</h3>
  <p class="blog-copy" style="left:833px;top:1572px">fringilla eu condimentum quis tellus Aenean porttitor eros vel dolor Donec convallis pede venenatis nibh Duis quam Nam eget lacus Aliquam erat</p>
  <span class="blog-more" style="left:833px;top:1680px">READ MORE</span>
</section>

<section class="testimonials">
  <h2 class="section-title" style="top:54px;font-size:25px;color:var(--ink)">TESTIMONIALS</h2>
  <span class="quote-mark" style="left:258px;top:86px">“</span>
  <p class="quote-text">Cras a ante vitae enim iaculis aliquam Mauris nunc quam venenatis nec euismod sit amet egestas placerat est Pellentesque habitant morbi tristique senectus et netus et malesuada fames ac turpis egestas Cras id elit Integer quis urna Ut ante enim dapibus malesuada fringilla eu condimentum quis</p>
  <span class="quote-mark" style="left:792px;top:160px">”</span>
  <div class="avatar" role="img" aria-label="Author portrait"></div>
  <p class="author">By Author Name<small>City Location</small></p>
  <div class="dots t-dots"><span class="dot on"></span><span class="dot"></span><span class="dot"></span><span class="dot"></span></div>
</section>

<footer class="footer">
  <h4 class="footer-head" style="left:189px">Company</h4>
  <ul class="footer-list" style="left:189px"><li>Home</li><li>About Us</li><li>Why Choose Us</li><li>Blog Post</li></ul>
  <div class="footer-divider" style="left:299px"></div>

  <h4 class="footer-head" style="left:322px">Services</h4>
  <ul class="footer-list" style="left:322px"><li>Personal Trainig</li><li>Fitness Coaching</li><li>Outdoor Bootcamp</li><li>Classes</li></ul>
  <div class="footer-divider" style="left:448px"></div>

  <h4 class="footer-head" style="left:483px;top:42px">Latest Tweet</h4>
  <div class="tweet" style="left:483px;top:70px"><span class="tweet-icon"></span><span class="tweet-handle">@DailyFitNote</span> susct varius mi.<br>Cum sociis natoque penabus et<br>1 day ago</div>
  <div class="tweet" style="left:483px;top:130px"><span class="tweet-icon"></span><span class="tweet-handle">@DailyFitNote</span> susct varius mi.<br>Cum sociis natoque penabus et<br>1 day ago</div>
  <div class="footer-divider" style="left:677px"></div>

  <h4 class="footer-head" style="left:713px">Contact Info</h4>
  <p class="contact-line" style="left:713px;top:74px">412 Alder Crest Way Suite B12<br>Kelwick, WA 98301</p>
  <p class="contact-line" style="left:713px;top:123px">
    <svg width="11" height="11" viewBox="0 0 24 24" style="vertical-align:-1px;margin-right:6px"><path fill="#ddd" d="M6.6 10.8a15 15 0 0 0 6.6 6.6l2.2-2.2c.3-.3.7-.4 1-.2 1.1.4 2.3.6 3.6.6.6 0 1 .4 1 1V20c0 .6-.4 1-1 1A17 17 0 0 1 3 4c0-.6.4-1 1-1h3.5c.6 0 1 .4 1 1 0 1.3.2 2.5.6 3.6.1.3 0 .7-.2 1z"/></svg>(555) 318-0427</p>
  <p class="contact-line" style="left:713px;top:145px">
    <svg width="11" height="9" viewBox="0 0 22 16" style="vertical-align:0;margin-right:6px"><rect width="22" height="16" rx="1" fill="#ddd"/><path d="M1 1 L11 9 L21 1" fill="none" stroke="#222" stroke-width="2"/></svg>info@valquor.com</p>

  <h4 class="footer-head" style="left:905px">Stay In Touch</h4>
  <div class="social"><span></span><span></span><span></span><span></span></div>
</footer>
<div class="footer-base"><p class="copyright">© 2016 Company Name &nbsp;All right reserved &nbsp;Term of Use</p></div>

</body>
</html>
```